Medical software helping patients with dry eye disease needs a business card

We have a logo we just need a design for a business card for a Canadian company called LUMA: Dry Eye. We use AI technology to assist optometrists in properly diagnosing patients with dry eye disease reducing wait times in doctors offices and accuracy of diagnosis as well as identifying key possible indicators and tailored treatment plans. The final design should be clean and medical looking. Our mission is to help patients and our logo using blues and whites.

```html
<!DOCTYPE html>
<html lang="en">
<head>
<meta charset="utf-8">
<title>LUMA: Dry Eye — Business Card</title>
<link rel="stylesheet" href="https://fonts.googleapis.com/css2?family=Lato:wght@400;700&family=Montserrat:wght@500;700;800&display=swap">
<style>
  :root {
    --stage: #1f2023;
    --white: #ffffff;
    --navy: #0f4a80;
    --navy-deep: #0b3c6b;
    --sky: #27a9e1;
    --ink: #2b2f36;
    --ink-soft: #4a5059;
  }
  * { box-sizing: border-box; margin: 0; padding: 0; }
  html, body { width: 1200px; height: 800px; overflow: hidden; }
  body {
    background: var(--stage);
    display: flex;
    align-items: center;
    justify-content: center;
    gap: 40px;
    font-family: "Lato", sans-serif;
  }
  .card {
    position: relative;
    width: 540px;
    height: 310px;
    border-radius: 16px;
    overflow: hidden;
  }

  /* Front */
  .card--front { background: var(--white); }
  .front-info {
    position: absolute;
    top: 78px;
    left: 0;
    right: 0;
    display: flex;
    justify-content: center;
    align-items: center;
    gap: 26px;
  }
  .identity { text-align: right; }
  .identity__name {
    font-family: "Montserrat", sans-serif;
    font-weight: 700;
    font-size: 24px;
    letter-spacing: 0.5px;
    color: var(--navy);
    line-height: 1.1;
  }
  .identity__title {
    font-family: "Montserrat", sans-serif;
    font-weight: 500;
    font-size: 17px;
    color: var(--sky);
    margin-top: 2px;
  }
  .divider { width: 2px; height: 82px; background: var(--navy); }
  .contacts { list-style: none; }
  .contacts__item {
    display: flex;
    align-items: center;
    gap: 9px;
    font-size: 14px;
    color: var(--ink-soft);
    line-height: 1.55;
  }
  .contacts__item--phone { font-size: 17px; font-weight: 700; color: var(--ink); }
  .contacts__item--web { font-weight: 700; color: var(--ink); }
  .contacts__icon { width: 13px; height: 13px; flex: none; }

  .address-band {
    position: absolute;
    left: 0;
    right: 0;
    top: 196px;
    height: 42px;
    background: var(--sky);
    display: flex;
    align-items: center;
    padding: 0 22px 0 34px;
    color: var(--white);
    font-size: 15px;
    gap: 8px;
  }
  .address-band__pin { width: 12px; height: 16px; flex: none; }
  .address-band__text { flex: 1; }
  .address-band__dot {
    width: 34px; height: 34px;
    border-radius: 50%;
    background: var(--navy);
    flex: none;
  }

  /* Back */
  .card--back { background: var(--navy); }
  .brand {
    position: absolute;
    top: 88px;
    left: 0;
    right: 0;
    display: flex;
    align-items: center;
    justify-content: center;
    gap: 16px;
  }
  .brand__dot {
    width: 56px; height: 56px;
    border-radius: 50%;
    background: var(--white);
  }
  .brand__name {
    font-family: "Montserrat", sans-serif;
    font-weight: 800;
    font-size: 52px;
    letter-spacing: 1px;
    color: var(--white);
  }
  .web-band {
    position: absolute;
    left: 0;
    right: 0;
    top: 210px;
    height: 46px;
    background: var(--sky);
    display: flex;
    align-items: center;
    justify-content: center;
    font-family: "Lato", sans-serif;
    font-size: 15px;
    letter-spacing: 6px;
    color: var(--white);
  }
  .card--back::after {
    content: "";
    position: absolute;
    left: 0; right: 0; bottom: 0;
    height: 54px;
    background: var(--navy-deep);
  }
</style>
</head>
<body>

  <section class="card card--front" aria-label="Business card front">
    <div class="front-info">
      <div class="identity">
        <p class="identity__name">DANIEL WHITFORD</p>
        <p class="identity__title">Founder &amp; CEO</p>
      </div>
      <div class="divider"></div>
      <ul class="contacts">
        <li class="contacts__item contacts__item--phone">
          <svg class="contacts__icon" viewBox="0 0 16 16"><path fill="#27a9e1" d="M3.2 1.5l2.4 2.6-1.3 2a9 9 0 0 0 5.6 5.6l2-1.3 2.6 2.4-1.6 2.2C6.4 16 0 9.6 1 3.1z"/></svg>
          403-555-0182
        </li>
        <li class="contacts__item">
          <svg class="contacts__icon" viewBox="0 0 16 16"><rect x="1" y="3" width="14" height="10" rx="1" fill="#27a9e1"/><path d="M1.5 4l6.5 5 6.5-5" fill="none" stroke="#fff" stroke-width="1.4"/></svg>
          info@lumadryeye.com
        </li>
        <li class="contacts__item contacts__item--web">
          <svg class="contacts__icon" viewBox="0 0 16 16"><circle cx="8" cy="8" r="7" fill="none" stroke="#27a9e1" stroke-width="1.6"/><path d="M1 8h14M8 1c-3 3.5-3 10.5 0 14M8 1c3 3.5 3 10.5 0 14" fill="none" stroke="#27a9e1" stroke-width="1.2"/></svg>
          LumaDryEye.com
        </li>
      </ul>
    </div>
    <div class="address-band">
      <svg class="address-band__pin" viewBox="0 0 12 16"><path fill="#fff" d="M6 0a6 6 0 0 0-6 6c0 4.5 6 10 6 10s6-5.5 6-10a6 6 0 0 0-6-6zm0 8.5A2.5 2.5 0 1 1 6 3.5a2.5 2.5 0 0 1 0 5z"/></svg>
      <span class="address-band__text">240 1125 54th Ave SW, Calgary, AB T2V 3K8</span>
      <span class="address-band__dot"></span>
    </div>
  </section>

  <section class="card card--back" aria-label="Business card back">
    <div class="brand">
      <span class="brand__dot"></span>
      <span class="brand__name">LUMA DRY EYE</span>
    </div>
    <div class="web-band">WWW.LUMADRYEYE.COM</div>
  </section>

</body>
</html>
```